50's-style gig poster for a birthday bash

My wife was born in 1957 and is turning 57 next month. I'm throwing a surprise party for her, and thought it would be fun to have a 18x24 poster printed and framed for the event. Attached is a poster from a Rufus Kettle gig in 1957. I'd like something like this, with a tinted B&W head shot of my wife, with similar fonts and background color schemes. The copy will be HELGA at the top (where the name RUFUS appears), with 57X57 under it, and the word Celebration where the word Quartet currently appears. The rest of the copy will be provided to you. Thanks for your interest and I look forward to working with you.

```html
<!DOCTYPE html>
<html lang="en">
<head>
<meta charset="utf-8">
<title>HELGA 57 x 57 Celebration</title>
<link rel="stylesheet" href="https://fonts.googleapis.com/css2?family=Oswald:wght@400&family=Lobster&family=Archivo+Narrow:wght@700&family=Archivo+Black&family=Roboto+Slab:wght@800&display=swap">
<style>
  :root {
    --cream: #f4ecd2;
    --stripe-red: #dd4a24;
    --stripe-blue: #2b3f9c;
    --yellow: #f5e51c;
    --white: #ffffff;
    --ink: #111111;
    --poster-red: #d8321c;
  }
  * { margin: 0; padding: 0; box-sizing: border-box; }
  html, body { width: 900px; height: 1200px; overflow: hidden; background: var(--cream); }
  .poster { position: relative; width: 900px; height: 1200px; background: var(--cream); }
  .stripes {
    position: absolute;
    left: 14px; top: 14px; right: 14px; bottom: 14px;
    background: linear-gradient(to right,
      var(--stripe-red) 0 271px,
      var(--stripe-blue) 271px 361px,
      var(--stripe-red) 361px 531px,
      var(--stripe-blue) 531px 626px,
      var(--stripe-red) 626px 872px);
  }
  .headline {
    position: absolute;
    left: 40px; right: 40px; top: 40px;
    display: flex; justify-content: space-between;
    padding: 0 20px;
    font-family: "Oswald", sans-serif;
    font-weight: 400;
    font-size: 180px;
    line-height: 1;
    color: var(--white);
  }
  .portrait {
    position: absolute;
    left: 135px; top: 330px;
    width: 290px; height: 465px;
    background: radial-gradient(ellipse at 60% 40%, #e2e2e2 0%, #a8a8a8 45%, #3e3e3e 100%);
    border: 3px solid var(--ink);
  }
  .age-burst {
    position: absolute;
    left: 280px; top: 235px;
    width: 180px; height: 120px;
    z-index: 2;
  }
  .age-burst text {
    font-family: "Archivo Black", sans-serif;
    font-size: 46px;
    fill: var(--poster-red);
  }
  .celebration {
    position: absolute;
    left: 455px; width: 350px; top: 245px;
    text-align: center;
    font-family: "Lobster", sans-serif;
    font-size: 58px;
    line-height: 70px;
    color: var(--yellow);
    -webkit-text-stroke: 1.5px var(--ink);
    transform: skewX(-8deg);
  }
  .featuring {
    position: absolute;
    left: 455px; width: 350px; top: 312px;
    text-align: center;
    font-family: "Lobster", sans-serif;
    font-size: 34px;
    line-height: 42px;
    color: var(--white);
  }
  .family-list {
    position: absolute;
    left: 445px; width: 370px; top: 358px;
    list-style: none;
    text-align: center;
    font-family: "Archivo Narrow", sans-serif;
    font-weight: 700;
    font-size: 32px;
    line-height: 41px;
    color: var(--white);
    text-shadow: 2px 2px 0 var(--ink);
  }
  .date-box {
    position: absolute;
    left: 445px; top: 660px;
    width: 335px; height: 205px;
    background: var(--white);
    border-radius: 18px;
    text-align: center;
    font-family: "Archivo Narrow", sans-serif;
    font-weight: 700;
    font-size: 46px;
    line-height: 58px;
    color: var(--stripe-blue);
    padding-top: 16px;
  }
  .also-appearing {
    position: absolute;
    left: 90px; top: 878px;
    font-family: "Lobster", sans-serif;
    font-size: 44px;
    line-height: 52px;
    color: var(--yellow);
    transform: skewX(-8deg);
  }
  .support-act {
    position: absolute;
    left: 60px; width: 780px; top: 925px;
    text-align: center;
    font-family: "Lobster", sans-serif;
    font-size: 66px;
    line-height: 80px;
    color: var(--yellow);
    -webkit-text-stroke: 1.5px var(--ink);
    transform: skewX(-8deg);
    white-space: nowrap;
  }
  .venue-box {
    position: absolute;
    left: 90px; top: 1030px;
    width: 726px; height: 128px;
    background: var(--white);
    border: 4px solid var(--ink);
    text-align: center;
    padding-top: 10px;
  }
  .venue-name {
    font-family: "Roboto Slab", serif;
    font-weight: 800;
    font-size: 50px;
    line-height: 60px;
    color: var(--ink);
    letter-spacing: 2px;
  }
  .venue-address {
    font-family: "Roboto Slab", serif;
    font-weight: 800;
    font-size: 30px;
    line-height: 44px;
    color: var(--stripe-blue);
  }
</style>
</head>
<body>
<div class="poster">
  <div class="stripes"></div>

  <h1 class="headline"><span>H</span><span>E</span><span>L</span><span>G</span><span>A</span></h1>

  <div class="portrait" role="img" aria-label="Tinted black and white head shot of Helga"></div>

  <svg class="age-burst" viewBox="-100 -100 200 200" preserveAspectRatio="none" aria-label="57 x 57">
    <polygon fill="#f5e51c" points="100,0 81,22 87,50 59,59 50,87 22,81 0,100 -22,81 -50,87 -59,59 -87,50 -81,22 -100,0 -81,-22 -87,-50 -59,-59 -50,-87 -22,-81 0,-100 22,-81 50,-87 59,-59 87,-50 81,-22"/>
    <text x="0" y="16" text-anchor="middle">57 x 57</text>
  </svg>

  <div class="celebration">Celebration</div>
  <div class="featuring">Featuring:</div>
  <ul class="family-list">
    <li>THE MARLOWES</li>
    <li>THE PENHALLOWS</li>
    <li>THE ASHBY-CROFTS</li>
    <li>THE THORNES</li>
    <li>THE GARRICKS</li>
  </ul>

  <div class="date-box">
    <div>One Night Only</div>
    <div>April 4, 2014</div>
    <div>6 PM</div>
  </div>

  <div class="also-appearing">Also Appearing</div>
  <div class="support-act">The Larks and Dot Fenwick</div>

  <div class="venue-box">
    <div class="venue-name">BISTRO VALMONT</div>
    <div class="venue-address">740 Alder Street, Paso Robles, California</div>
  </div>
</div>
</body>
</html>
```